TOLV.
RAKESH ENTERTAINMENT & MEDIA
Use specific fonts
any thing which suits with the LOGO provided
Professional
RAKESH MEHTA
MR.
D-47, NORTH PARK-II , GURGAON 122001,HARYANA, INDIA
rakesh@tolv.co.in
www.tolv.co.in
LOG IN THE CENTRE

```html
<!DOCTYPE html>
<html lang="en">
<head>
<meta charset="utf-8">
<title>TOLV Stationery</title>
<link href="https://fonts.googleapis.com/css2?family=Open+Sans:wght@400;700&display=swap" rel="stylesheet">
<style>
:root{
  --stage:#3a3a3c;
  --paper:#ffffff;
  --brand:#1a7fa6;
  --brand-deep:#0d5a7c;
  --ink:#3b4a55;
  --muted:#9a9fa4;
  --env:#eef2f5;
  --env-edge:#d5dde3;
}
*{margin:0;padding:0;box-sizing:border-box}
html,body{width:1200px;height:348px;overflow:hidden;background:var(--stage);font-family:"Open Sans",Arial,sans-serif}
.sheet{position:relative;width:1200px;height:348px}
.piece{position:absolute;background:var(--paper);overflow:hidden;box-shadow:0 2px 6px rgba(0,0,0,.45)}
.piece svg.band{position:absolute;left:0;top:0;width:100%;height:100%}
.label{position:absolute;font-size:6px;color:var(--muted);text-align:center;white-space:nowrap}
.logo{position:absolute;display:flex;align-items:center;gap:3px;font-weight:700;color:var(--brand);line-height:1;white-space:nowrap}
.logo .mark{background:var(--brand);display:block}
.tiny{position:absolute;font-size:4px;line-height:1.45;color:var(--ink);white-space:nowrap}
.tiny.light{color:#e6f3f8}
.tiny.right{text-align:right}
.tiny.center{text-align:center;left:0;right:0}
</style>
</head>
<body>
<div class="sheet">

  <div class="label" style="left:29px;top:138px">Business Cards</div>

  <!-- business card front -->
  <div class="piece card-front" style="left:29px;top:149px;width:129px;height:72px">
    <svg class="band" viewBox="0 0 129 72" preserveAspectRatio="none">
      <path d="M0 0H129V14C90 12 60 18 0 30Z" fill="var(--brand)"/>
      <path d="M0 30C60 18 90 12 129 14V17C90 15 60 21 0 33Z" fill="var(--brand-deep)"/>
    </svg>
    <div class="tiny light right" style="right:6px;top:3px">RAKESH MEHTA<br>MR.</div>
    <div class="tiny right" style="right:6px;top:36px">RAKESH ENTERTAINMENT &amp; MEDIA<br>D-47, NORTH PARK-II , GURGAON<br>122001,HARYANA, INDIA<br>rakesh@tolv.co.in<br>www.tolv.co.in</div>
  </div>

  <!-- business card back -->
  <div class="piece card-back" style="left:29px;top:235px;width:129px;height:72px">
    <div class="logo" style="left:46px;top:28px;font-size:13px"><span class="mark" style="width:6px;height:6px"></span>TOLV</div>
  </div>
  <div class="label" style="left:29px;top:312px;width:129px">Card Back</div>

  <!-- letterhead one -->
  <div class="piece letterhead" style="left:168px;top:24px;width:223px;height:288px">
    <svg class="band" viewBox="0 0 223 288" preserveAspectRatio="none">
      <path d="M100 0H223V22C180 20 140 26 112 40C108 24 104 10 100 0Z" fill="var(--brand)"/>
      <path d="M0 50C70 40 150 16 223 22V25C150 20 70 44 0 54Z" fill="var(--brand-deep)"/>
    </svg>
    <div class="logo" style="left:12px;top:10px;font-size:20px"><span class="mark" style="width:8px;height:8px"></span>TOLV</div>
    <div class="tiny light" style="left:152px;top:3px">rakesh@tolv.co.in<br>www.tolv.co.in</div>
  </div>
  <div class="label" style="left:168px;top:318px;width:223px">Letterhead</div>

  <!-- letterhead two -->
  <div class="piece letterhead" style="left:408px;top:24px;width:223px;height:288px">
    <svg class="band" viewBox="0 0 223 288" preserveAspectRatio="none">
      <path d="M100 0H223V22C180 20 140 26 112 40C108 24 104 10 100 0Z" fill="var(--brand)"/>
      <path d="M0 50C70 40 150 16 223 22V25C150 20 70 44 0 54Z" fill="var(--brand-deep)"/>
    </svg>
    <div class="logo" style="left:34px;top:22px;font-size:20px"><span class="mark" style="width:8px;height:8px"></span>TOLV</div>
    <div class="tiny center" style="top:272px">D-47, NORTH PARK-II , GURGAON 122001,HARYANA, INDIA<br>rakesh@tolv.co.in · www.tolv.co.in</div>
  </div>
  <div class="label" style="left:408px;top:318px;width:223px">Letterhead</div>

  <!-- compliment slip one -->
  <div class="piece slip" style="left:643px;top:58px;width:252px;height:100px">
    <svg class="band" viewBox="0 0 252 100" preserveAspectRatio="none">
      <path d="M120 0H252V20C200 18 160 22 130 32C126 18 123 8 120 0Z" fill="var(--brand)"/>
      <path d="M0 36C80 32 170 12 252 20V23C170 16 80 36 0 39Z" fill="var(--brand-deep)"/>
    </svg>
    <div class="logo" style="left:10px;top:10px;font-size:18px"><span class="mark" style="width:7px;height:7px"></span>TOLV</div>
    <div class="tiny" style="left:10px;top:34px">rakesh@tolv.co.in</div>
  </div>
  <div class="label" style="left:643px;top:164px;width:252px">Compliment Slip</div>

  <!-- compliment slip two -->
  <div class="piece slip" style="left:643px;top:204px;width:252px;height:100px">
    <svg class="band" viewBox="0 0 252 100" preserveAspectRatio="none">
      <path d="M120 0H252V20C200 18 160 22 130 32C126 18 123 8 120 0Z" fill="var(--brand)"/>
      <path d="M0 36C80 32 170 12 252 20V23C170 16 80 36 0 39Z" fill="var(--brand-deep)"/>
    </svg>
    <div class="logo" style="left:10px;top:10px;font-size:18px"><span class="mark" style="width:7px;height:7px"></span>TOLV</div>
    <div class="tiny center" style="top:88px">D-47, NORTH PARK-II , GURGAON 122001,HARYANA, INDIA</div>
  </div>
  <div class="label" style="left:643px;top:310px;width:252px">Compliment Slip</div>

  <!-- envelope front -->
  <div class="piece envelope" style="left:907px;top:67px;width:264px;height:100px">
    <svg class="band" viewBox="0 0 264 100" preserveAspectRatio="none">
      <path d="M110 0H264V20C210 18 160 22 130 32C124 18 116 8 110 0Z" fill="var(--brand)"/>
      <path d="M60 38C120 32 190 16 264 20V23C190 20 120 36 60 41Z" fill="var(--brand-deep)"/>
    </svg>
    <div class="logo" style="left:150px;top:6px;font-size:8px;color:#ffffff"><span class="mark" style="width:4px;height:4px;background:#ffffff"></span>TOLV</div>
  </div>

  <!-- envelope back -->
  <div class="piece envelope" style="left:907px;top:197px;width:264px;height:100px;background:var(--env)">
    <svg class="band" viewBox="0 0 264 100" preserveAspectRatio="none">
      <path d="M0 0H264V14C200 12 160 20 132 44C104 20 64 12 0 14Z" fill="var(--brand)"/>
      <path d="M0 100L118 50M264 100L146 50" stroke="var(--env-edge)" stroke-width="1" fill="none"/>
    </svg>
    <div class="logo" style="left:116px;top:58px;font-size:8px"><span class="mark" style="width:4px;height:4px"></span>TOLV</div>
  </div>
  <div class="label" style="left:907px;top:303px;width:264px">Envelope</div>

</div>
</body>
</html>
```